Packaging design for Organic Beard Care brand - Talon Meadows

This packaging design will be for our beard oil collection which include five different beard oil scents and our signature blend beard oil which is separate from the collection.
There will be two different variants of the box design needed:
Variant 1: White box with Logo and text (Ingredients, Directions, etc).
The words “Handcrafted Premium Beard Oil” will be printed in green foil color. Work this into the design.
Variant 2: Black box with gold foil logo and gold foil text (Ingredients, Directions, etc).
The words “Handcrafted Premium Beard Oil” will be printed in gold foil color. Work this into the design.
Both boxes should have a premium look and feel to it without too much noise.
(Think Brisk deodorant & shampoo brand or Plume teeth whitening brand)
Key callouts will be provided to add to the box designs.
I’ve attached icons, logos, images of the beard oil products and UPC codes that should be used on each box variant.
Please message me if there are more image assets or questions you have about creating the package design.
**Important** - You must create the design on the template file: 30ml-cardboard-box-template-talon-meadows.ai. Any submissions without the design within this template will be passed up/rejected.
Men 21-50
Health & Beauty Cosmetics
- Miso, ASAP Condensed

```html
<!DOCTYPE html>
<html lang="en">
<head>
<meta charset="utf-8">
<title>Talon Meadows – Beard Oil Box, Variant 2</title>
<link href="https://fonts.googleapis.com/css2?family=Asap+Condensed:wght@400;500;600&family=Barlow+Condensed:wght@500;600&display=swap" rel="stylesheet">
<style>
  :root {
    --paper: #ffffff;
    --board: #231f20;
    --cut-line: #e0321c;
    --gold: #d9b552;
    --gold-dim: #7a6537;
    --label-grey: #dcdcdc;
    --upc-fill: #3a3839;
    --upc-text: #4a4849;
  }
  html, body {
    margin: 0;
    padding: 0;
    width: 954px;
    height: 1200px;
    overflow: hidden;
    background: var(--paper);
  }
  .dieline { display: block; width: 954px; height: 1200px; }
  .panel { fill: var(--board); stroke: var(--cut-line); stroke-width: 2; }
  .fold { fill: none; stroke: var(--cut-line); stroke-width: 2; }
  .variant-label { font-family: "Barlow Condensed", sans-serif; font-weight: 500; font-size: 84px; fill: var(--label-grey); }
  .brand-name { font-family: "Asap Condensed", sans-serif; font-weight: 600; fill: var(--gold); text-anchor: middle; }
  .brand-name--faint { fill: var(--gold-dim); }
  .headline { font-family: "Barlow Condensed", sans-serif; font-weight: 600; font-size: 54px; fill: var(--gold); text-anchor: middle; letter-spacing: 0.5px; }
  .subhead { font-family: "Barlow Condensed", sans-serif; font-weight: 500; font-size: 31px; fill: var(--gold); text-anchor: middle; letter-spacing: 0.5px; }
  .rule { stroke: var(--gold); stroke-width: 2; }
  .callout { font-family: "Asap Condensed", sans-serif; font-weight: 500; font-size: 19px; fill: var(--gold); text-anchor: middle; }
  .copy { font-family: "Asap Condensed", sans-serif; font-weight: 400; font-size: 19px; fill: var(--gold-dim); text-anchor: middle; }
  .web { font-family: "Asap Condensed", sans-serif; font-weight: 500; font-size: 20px; fill: var(--gold); text-anchor: middle; }
  .badge { fill: var(--gold); }
  .upc-area { fill: var(--upc-fill); }
  .upc-label { font-family: "Asap Condensed", sans-serif; font-size: 36px; fill: var(--upc-text); text-anchor: middle; }
</style>
</head>
<body>
<svg class="dieline" viewBox="0 0 1718 2160" xmlns="http://www.w3.org/2000/svg">
  <text class="variant-label" x="118" y="178">Variant 2</text>

  <!-- glue flap -->
  <polygon class="panel" points="131,620 237,595 237,1568 131,1543"/>

  <!-- side and face panels -->
  <rect class="panel" x="237" y="595" width="340" height="973"/>
  <rect class="panel" x="577" y="595" width="338" height="973"/>
  <rect class="panel" x="915" y="592" width="339" height="980"/>
  <rect class="panel" x="1254" y="595" width="334" height="973"/>

  <!-- top closure -->
  <rect class="panel" x="915" y="253" width="339" height="339"/>
  <path class="panel" d="M920,253 V215 Q920,145 990,145 H1179 Q1249,145 1249,215 V253 Z"/>
  <path class="fold" d="M986,265 V257 H1183 V265"/>

  <!-- bottom closure -->
  <rect class="panel" x="915" y="1572" width="339" height="340"/>
  <path class="panel" d="M920,1912 V1948 Q920,2018 990,2018 H1179 Q1249,2018 1249,1948 V1912 Z"/>
  <path class="fold" d="M986,1898 V1906 H1183 V1898"/>

  <!-- dust flaps -->
  <polygon class="panel" points="612,452 892,452 892,572 903,595 581,595 581,543 602,520"/>
  <polygon class="panel" points="1276,452 1555,452 1566,520 1588,543 1588,595 1266,595 1276,572"/>
  <polygon class="panel" points="581,1568 903,1568 892,1592 892,1712 612,1712 602,1643 581,1622"/>
  <polygon class="panel" points="1266,1568 1588,1568 1588,1622 1566,1643 1555,1712 1276,1712 1276,1592"/>

  <!-- top panel -->
  <text class="brand-name" x="1084" y="432" font-size="42">Talon Meadows</text>

  <!-- side front panel -->
  <g class="front-face">
    <text class="brand-name" x="408" y="815" font-size="46">Talon Meadows</text>
    <line class="rule" x1="283" y1="1051" x2="535" y2="1051"/>
    <text class="headline" x="408" y="1120">HANDCRAFTED</text>
    <text class="subhead" x="408" y="1158">PREMIUM BEARD OIL</text>
    <line class="rule" x1="283" y1="1190" x2="535" y2="1190"/>
    <text class="callout" x="408" y="1339">Made with 100% All-Natural &amp;</text>
    <text class="callout" x="408" y="1367">Organic Ingredients.</text>
    <text class="callout" x="408" y="1395">None of that artificial stuff!</text>
    <text class="callout" x="408" y="1456">1 FL OZ/30 ml</text>
  </g>

  <!-- directions panel -->
  <g class="directions-face">
    <text class="brand-name brand-name--faint" x="745" y="902" font-size="28">Talon Meadows</text>
    <text class="copy" x="745" y="1010">Directions:</text>
    <text class="copy" x="745" y="1050">Squeeze 1-2 pulls of oil to the</text>
    <text class="copy" x="745" y="1077">palm of your hand. For longer</text>
    <text class="copy" x="745" y="1104">beards, use 3-4 pulls of oil. Rub</text>
    <text class="copy" x="745" y="1131">hands together and massage into</text>
    <text class="copy" x="745" y="1158">beard . Finish by styling as usual</text>
    <text class="copy" x="745" y="1185">with a beard comb or pick to</text>
    <text class="copy" x="745" y="1212">spread beard oil evenly</text>
    <text class="copy" x="745" y="1238">throughout your beard. Use daily</text>
    <text class="copy" x="745" y="1264">for best results.</text>
  </g>

  <!-- main front panel -->
  <g class="front-face">
    <text class="brand-name" x="1084" y="815" font-size="46">Talon Meadows</text>
    <line class="rule" x1="958" y1="1051" x2="1210" y2="1051"/>
    <text class="headline" x="1084" y="1120">HANDCRAFTED</text>
    <text class="subhead" x="1084" y="1158">PREMIUM BEARD OIL</text>
    <line class="rule" x1="958" y1="1190" x2="1210" y2="1190"/>
    <text class="callout" x="1084" y="1339">Made with 100% All-Natural &amp;</text>
    <text class="callout" x="1084" y="1367">Organic Ingredients.</text>
    <text class="callout" x="1084" y="1395">None of that artificial stuff!</text>
    <text class="callout" x="1084" y="1456">1 FL OZ/30 ml</text>
  </g>

  <!-- story panel -->
  <g class="story-face">
    <text class="brand-name brand-name--faint" x="1420" y="738" font-size="28">Talon Meadows</text>
    <text class="copy" x="1420" y="835">Talon Meadows was created out</text>
    <text class="copy" x="1420" y="861">of a necessity to provide beard</text>
    <text class="copy" x="1420" y="888">oils that are made with natural</text>
    <text class="copy" x="1420" y="915">and organic ingredients that</text>
    <text class="copy" x="1420" y="942">would not be harmful to men who</text>
    <text class="copy" x="1420" y="968">have skin sensitivities to heavy</text>
    <text class="copy" x="1420" y="995">fragrances and artificial fillers.</text>
    <text class="copy" x="1420" y="1048">We have helped thousands of</text>
    <text class="copy" x="1420" y="1075">men keep their beards healthy</text>
    <text class="copy" x="1420" y="1102">and smelling good for over half a</text>
    <text class="copy" x="1420" y="1128">decade with amazing products</text>
    <text class="copy" x="1420" y="1155">and solid education on the many</text>
    <text class="copy" x="1420" y="1182">types of oils and ingredients that</text>
    <text class="copy" x="1420" y="1209">go into our beard oils and other</text>
    <text class="copy" x="1420" y="1235">beard care products.</text>
    <text class="copy" x="1420" y="1289">Our beard oils have been proven</text>
    <text class="copy" x="1420" y="1315">to prevent beard itch and beard</text>
    <text class="copy" x="1420" y="1342">dandruff while keeping your</text>
    <text class="copy" x="1420" y="1369">beard feeling soft and</text>
    <text class="copy" x="1420" y="1396">manageable everyday. Quality</text>
    <text class="copy" x="1420" y="1422">Ingredients. Quality Service.</text>
    <text class="copy" x="1420" y="1449">Everyday.</text>
  </g>

  <!-- bottom panel -->
  <g class="base-face">
    <rect class="badge" x="998" y="1618" width="52" height="40" rx="3"/>
    <rect class="badge" x="1067" y="1618" width="44" height="40" rx="3"/>
    <circle class="badge" cx="1149" cy="1638" r="21"/>
    <text class="web" x="1084" y="1686">www.talonmeadows.com</text>
    <rect class="upc-area" x="970" y="1702" width="229" height="165"/>
    <text class="upc-label" x="1084" y="1797">UPC code</text>
  </g>
</svg>
</body>
</html>
```